Personal logo & business cards
for owner of multiple businesses.
Hi qlindo,
I really like your design #16. Can you maybe try it in a couple different colour combinations, and maybe also with the 'MIRELA VOSK' part in a cursive text?
Thanks,
Mirela
Hello porvadesign:
I like the design on 19 & 20, but I'd prefer it without the logo on the front. Also, there's maybe too much purple... it's a bit too feminine. Can you try it with less purple or in another colour?
Thanks!
I don't currently have a logo or anything... and would prefer that there wasn't a logo for one of my businesses on the front of my card. A personal logo would be okay though.
@PH - Any logo to use? Thanks
Hey everyone,
Please make sure to read the brief a little more closely. I only want my name and personal contact information on the front of the card, and the names of the THREE businesses that I am involved in on the back of the card.
Thanks for your submissions!
Open to colour palette, but leaning more towards purple or green. No blues.

```html
<!DOCTYPE html>
<html lang="en">
<head>
<meta charset="utf-8">
<title>Mirela Vosk — Business Cards</title>
<link href="https://fonts.googleapis.com/css2?family=Open+Sans:wght@400;600;700&display=swap" rel="stylesheet">
<style>
  :root{
    --bg:#e9e6e2;
    --card:#ffffff;
    --ink:#333333;
    --ink-soft:#555555;
    --plum:#7a2a6e;
    --magenta:#c63b8e;
    --green:#6fae3a;
    --green-light:#a6cf5e;
    --tint:#f3e8ef;
  }
  *{box-sizing:border-box;margin:0;padding:0}
  html,body{width:1200px;height:1037px;overflow:hidden}
  body{background:var(--bg);font-family:"Open Sans",Arial,sans-serif;color:var(--ink);position:relative}
  .card{position:absolute;background:var(--card);box-shadow:0 6px 18px rgba(0,0,0,.18);overflow:hidden}
  .card--front{left:112px;top:79px;width:703px;height:421px}
  .card--back{left:385px;top:542px;width:708px;height:427px}

  .wordmark{position:absolute;left:60px;top:42px;display:flex;align-items:center;gap:18px}
  .wordmark__square{width:44px;height:44px;background:var(--plum);border-radius:5px}
  .wordmark__name{font-size:58px;font-weight:400;letter-spacing:1px;color:var(--ink);line-height:1}

  .name-band{position:absolute;left:0;top:217px;width:703px;height:38px;display:flex}
  .name-band__tab{width:56px;background:linear-gradient(90deg,var(--green),var(--green-light))}
  .name-band__bar{flex:1;margin-left:10px;background:linear-gradient(90deg,var(--plum),var(--magenta) 70%,#e9b6d4);display:flex;align-items:center;padding-left:16px}
  .name-band__name{color:#fff;font-weight:700;font-size:23px}

  .address{position:absolute;left:56px;top:290px;font-size:17px;line-height:28px;color:var(--ink-soft)}
  .divider{position:absolute;left:286px;top:282px;width:2px;height:76px;background:#555}
  .contacts{position:absolute;left:306px;top:276px;list-style:none;font-size:17px;color:var(--ink-soft)}
  .contacts li{display:flex;align-items:center;gap:14px;height:29px}
  .contacts svg{width:18px;height:20px;flex:none}
  .contacts .at{width:18px;text-align:center;font-weight:700;color:var(--ink)}

  .site{position:absolute;font-weight:700;color:var(--ink)}
  .card--front .site{left:0;width:100%;text-align:center;top:375px;font-size:20px}

  .accent-square{position:absolute;background:var(--tint);border-radius:12px}
  .card--front .accent-square{right:40px;top:180px;width:110px;height:110px;opacity:.7}
  .card--back .accent-square{right:60px;top:50px;width:150px;height:150px}

  .ventures{position:absolute;left:44px;top:36px;list-style:none;font-size:21px;line-height:28px;color:var(--ink)}
  .ventures li{margin-bottom:28px}

  .site-band{position:absolute;left:0;top:300px;width:708px;height:40px;display:flex}
  .site-band__bar{flex:1;background:linear-gradient(90deg,#e9b6d4,var(--magenta) 35%,var(--plum));display:flex;align-items:center;justify-content:flex-end;padding-right:20px}
  .site-band__bar .site{position:static;color:#fff;font-size:25px}
  .site-band__tab{width:46px;margin-left:10px;background:linear-gradient(90deg,var(--green-light),var(--green))}
</style>
</head>
<body>
  <section class="card card--front" aria-label="Card front">
    <div class="accent-square"></div>
    <div class="wordmark">
      <span class="wordmark__square"></span>
      <span class="wordmark__name">MIRELA VOSK</span>
    </div>
    <div class="name-band">
      <div class="name-band__tab"></div>
      <div class="name-band__bar"><span class="name-band__name">Mirela Vosk Trosdan</span></div>
    </div>
    <p class="address">208, 4431 9 Avenue NE<br>Halden, AB T5K 3R7</p>
    <div class="divider"></div>
    <ul class="contacts">
      <li>
        <svg viewBox="0 0 18 20"><rect x="5" y="1" width="8" height="18" rx="2" fill="#333"/><rect x="6.5" y="3.5" width="5" height="9" fill="#fff"/></svg>
        555-214-0387
      </li>
      <li>
        <svg viewBox="0 0 18 20"><path d="M2 14 L4 8 Q5 6 7 6 H11 Q13 6 14 8 L16 14 V17 H13 V15.5 H5 V17 H2 Z" fill="#333"/><rect x="5" y="8" width="8" height="3" fill="#fff"/></svg>
        555-608-9142
      </li>
      <li><span class="at">@</span>mirelatrosdan@mailvo.com</li>
    </ul>
    <p class="site">www.mirelavosk.com</p>
  </section>

  <section class="card card--back" aria-label="Card back">
    <div class="accent-square"></div>
    <ul class="ventures">
      <li>Mirela Vosk's Liquidation Supercentre<br>President.</li>
      <li>Sharp Deals @ Silly Prices<br>President.</li>
      <li>Trosdan Group<br>Partner.</li>
    </ul>
    <div class="site-band">
      <div class="site-band__bar"><span class="site">www.mirelavosk.com</span></div>
      <div class="site-band__tab"></div>
    </div>
  </section>
</body>
</html>
```